Dental Patient Education Single page-Multiple pages needed.

I am creating a unique dental patient education materials for resale. I work in the dental industry, training dentists and thier teams how to improve patient acceptance rates for treatment. I see a need that all patient education material is designed incorrectly. I want to fix this by creating patient education material that educated patients based on all of the treatment options for a diagnosed condition. Tradidional patient education material reads like a catalog of procedures. This format is not effective for helping the patient quickly understand the consequences of non treatment and the benefits and disadvantages of their treatment options. Specifics of the Job:The design images must be royalty free.I will provide the text.Initially there are for major diagnosed conditions: Infected Tooth Treatment Options, Single to Multiple Missing tooth Treatment Options, Full Arch of Missing Teeth Treatment Options, and Full Arch Fixed Dental Implant Treatment OptionsThe layout should mirror the attached sample of Single Missing Tooth Treatment Options.This is a project that will require edits and redesigned based on testing.I also need this in Adobe, so it can be customized/branded for a dental office.

Target Market(s)

Dental office professionals to educate patients.

Font styles to use
Sans Serif

Colors
3277b5

Requirements
Must have
• Professional look and feel
• Royalty free images
• Easy to read

```html
<!DOCTYPE html>
<html lang="en">
<head>
<meta charset="utf-8">
<title>Single Missing Tooth – Your Options For Treatment</title>
<link rel="stylesheet" href="https://fonts.googleapis.com/css2?family=Exo+2:ital,wght@0,400;0,600;0,700;0,800;1,600;1,700;1,800&family=Montserrat:wght@400;600;700&display=swap">
<style>
  :root{
    --blue:#1594c3;
    --blue-light:#19a3cf;
    --blue-deep:#0b5f85;
    --navy:#17344a;
    --heading:#3b6d95;
    --ink:#2b2b2b;
    --paper:#ffffff;
    --tile:#eef1f3;
    --gum:#e89a9c;
  }
  *{box-sizing:border-box;margin:0;padding:0}
  html,body{width:848px;height:1200px;overflow:hidden;background:var(--paper)}
  .sheet{position:relative;width:848px;height:1200px;background:var(--paper);font-family:"Montserrat",Arial,sans-serif;color:var(--ink)}

  .hero{position:absolute;left:0;top:0;width:848px;height:418px}
  .hero svg{position:absolute;inset:0}
  .hero-visual{position:absolute;left:470px;top:18px;width:360px;height:290px;border-radius:50%;
    background:radial-gradient(ellipse at 50% 45%,#fdfdfd 0%,#e4e7ea 55%,rgba(255,255,255,0) 75%)}
  .hero-title{position:absolute;font-family:"Exo 2",Arial,sans-serif;font-weight:800;line-height:1}
  .t-single{left:57px;top:154px;font-size:31px;font-weight:700;color:var(--paper)}
  .t-your{left:10px;top:198px;font-size:44px;font-style:italic;color:var(--navy)}
  .t-options{left:99px;top:182px;font-size:60px;font-style:italic;color:var(--paper)}
  .t-treatment{left:134px;top:260px;font-size:46px;font-style:italic;color:var(--navy)}
  .hero-intro{position:absolute;left:21px;top:336px;width:540px;font-size:14px;font-weight:600;line-height:17px;color:var(--paper)}

  .lead{position:absolute;left:0;top:432px;width:848px;text-align:center;font-family:"Exo 2",Arial,sans-serif;color:var(--navy);line-height:22px}
  .lead .practice{font-weight:700;font-size:22px;letter-spacing:1px;color:var(--blue-deep);word-spacing:8px}
  .lead .has{font-style:italic;font-weight:600;font-size:19px;word-spacing:8px;margin-left:8px}
  .lead .line2{font-style:italic;font-weight:600;font-size:18.5px;padding-left:36px}

  .option{position:absolute;left:0;width:848px;height:148px}
  .chevron{position:absolute;left:18px;top:0;width:202px;height:148px}
  .chevron-label{position:absolute;left:70px;top:54px;font-family:"Exo 2",Arial,sans-serif;font-style:italic;font-weight:600;font-size:30px;color:var(--paper);line-height:1}
  .option-text{position:absolute;left:234px;width:334px}
  .option-title{font-family:"Exo 2",Arial,sans-serif;font-style:italic;font-weight:700;font-size:19px;color:var(--heading);margin-bottom:6px;line-height:1}
  .option-body{font-size:10.3px;line-height:11.6px;color:var(--ink)}
  .option-visual{position:absolute}
  .visual-photo{left:588px;top:0;width:237px;height:148px;background:linear-gradient(135deg,#efeae6 0%,#c99a86 55%,#6b4a3e 100%)}
  .visual-diagram{left:568px;width:259px;height:140px;background:linear-gradient(180deg,#f3c3c4 0%,#e89a9c 40%,#fbf7f5 70%,#ffffff 100%);border-radius:6px}

  .footer-band{position:absolute;left:0;bottom:0;width:848px;height:25px;background:linear-gradient(90deg,var(--blue-deep),var(--blue-light) 50%,var(--blue-deep))}
</style>
</head>
<body>
<main class="sheet">

  <header class="hero">
    <svg width="848" height="418" viewBox="0 0 848 418" aria-hidden="true">
      <defs>
        <linearGradient id="heroBlue" x1="0" y1="0" x2="1" y2="1">
          <stop offset="0" stop-color="#0e78a6"/>
          <stop offset="0.5" stop-color="#1594c3"/>
          <stop offset="1" stop-color="#19a3cf"/>
        </linearGradient>
      </defs>
      <rect width="848" height="418" fill="url(#heroBlue)"/>
      <path d="M250 0 L427 0 L300 140 Z" fill="#ffffff" opacity="0.08"/>
      <path d="M848 228 L782 336 C750 392 690 408 640 368 L420 170 C375 128 380 60 427 0 L848 0 Z" fill="#0b5f85"/>
      <path d="M848 217 L772 330 C742 380 690 392 645 352 L420 160 C378 122 380 58 427 0 L848 0 Z" fill="#ffffff"/>
    </svg>
    <div class="hero-visual" role="img" aria-label="Illustration of a white molar beside a titanium dental implant screw and crown"></div>
    <div class="hero-title t-single">Single Missing Tooth</div>
    <div class="hero-title t-your">Your</div>
    <div class="hero-title t-options">Options</div>
    <div class="hero-title t-treatment">For Treatment</div>
    <p class="hero-intro">A missing tooth is a serious issue. It can cause long-term damage to facial structure, bone density and your ability to feel confident in your smile.</p>
  </header>

  <section class="lead">
    <div><span class="practice">MAPLE GROVE DENTAL CENTER</span><span class="has">has several</span></div>
    <div class="line2">options available to fix your missing tooth.</div>
  </section>

  <svg width="0" height="0" style="position:absolute" aria-hidden="true">
    <defs>
      <linearGradient id="chevronBlue" x1="0" y1="0" x2="1" y2="0">
        <stop offset="0" stop-color="#0b5f85"/>
        <stop offset="0.5" stop-color="#1594c3"/>
        <stop offset="1" stop-color="#19a3cf"/>
      </linearGradient>
    </defs>
  </svg>

  <article class="option" style="top:500px">
    <svg class="chevron" viewBox="0 0 202 148" aria-hidden="true"><path d="M0 0 H140 Q146 0 150 5 L202 74 L150 143 Q146 148 140 148 H0 L52 74 Z" fill="url(#chevronBlue)"/></svg>
    <div class="chevron-label">OPTION 1</div>
    <div class="option-text" style="top:44px">
      <h2 class="option-title">Do Nothing</h2>
      <p class="option-body">If you choose to do nothing at this time, the cost down the road can be substantial. <b>$10,000+</b> for orthodontics to straighten out the teeth, implant abutment and crown, bone grafting and possible sinus lift to replace lost bone.</p>
    </div>
    <div class="option-visual visual-photo" role="img" aria-label="Photo of a smiling mouth with a gap from a missing front tooth"></div>
  </article>

  <article class="option" style="top:670px">
    <svg class="chevron" viewBox="0 0 202 148" aria-hidden="true"><path d="M0 0 H140 Q146 0 150 5 L202 74 L150 143 Q146 148 140 148 H0 L52 74 Z" fill="url(#chevronBlue)"/></svg>
    <div class="chevron-label">OPTION 2</div>
    <div class="option-text" style="top:15px">
      <h2 class="option-title">Dental Implant</h2>
      <p class="option-body">The <b><i>bad</i></b> news is that a dental implant is the most expensive option, <b>BUT</b> the good news is it is the most effective, functional and aesthetically pleasing. A dental implant will keep the bone in that area of the jaw from atrophy. It helps maintain face shape and prevents 'sunken face'. The implant will prevent surrounding teeth from shifting and chances of losing the tooth decline. It will keep the teeth from shifting, and will prevent any future need to cut down the adjacent teeth. A dental implant is the nearest thing to a natural tooth available today.</p>
    </div>
    <div class="option-visual visual-diagram" style="top:4px" role="img" aria-label="Diagram of an upper arch showing implant, abutment and crown replacing one tooth"></div>
  </article>

  <article class="option" style="top:843px">
    <svg class="chevron" viewBox="0 0 202 148" aria-hidden="true"><path d="M0 0 H140 Q146 0 150 5 L202 74 L150 143 Q146 148 140 148 H0 L52 74 Z" fill="url(#chevronBlue)"/></svg>
    <div class="chevron-label">OPTION 3</div>
    <div class="option-text" style="top:32px">
      <h2 class="option-title">Dental Bridge</h2>
      <p class="option-body">The <b>good</b> news here is that a bridge is less expensive than the implant option BUT you will continue to lose bone in that area over time. Food will get caught in the hard to reach areas and if not cleaned properly could mean you have to replace the bridge every 7 years. In addition, to secure the bridge, the adjacent teeth must be cut down in order to be used as anchors for the appliance. Why cut down two good teeth if we don't have to?</p>
    </div>
    <div class="option-visual visual-diagram" style="top:4px" role="img" aria-label="Diagram of an upper arch with a three-unit bridge fitting over two prepared teeth"></div>
  </article>

  <article class="option" style="top:1012px">
    <svg class="chevron" viewBox="0 0 202 148" aria-hidden="true"><path d="M0 0 H140 Q146 0 150 5 L202 74 L150 143 Q146 148 140 148 H0 L52 74 Z" fill="url(#chevronBlue)"/></svg>
    <div class="chevron-label">OPTION 4</div>
    <div class="option-text" style="top:42px">
      <h2 class="option-title">The Removable Partial Denture (RPO)</h2>
      <p class="option-body">The good news here is that it's the least expensive option of the 3, but the <b>BAD</b> news is that your teeth have to come out every night. You won't be able to chew your food as well and your tongue will be uncomfortable with the big, bulky plastic sitting in your mouth all day.</p>
    </div>
    <div class="option-visual visual-diagram" style="top:0" role="img" aria-label="Diagram of an upper arch with a removable partial denture and clasps"></div>
  </article>

  <div class="footer-band" aria-hidden="true"></div>
</main>
</body>
</html>
```